Flyer für Veranstaltungstechnik-Unternehmen
Zielgruppe
VERANSTALTUNGSTECHNIK
Aufgabenstellung
Wir haben diesen Flyer erhalten, finden ihn aber nicht ansprechend, sehr altmodisch und möchten einen klar strukturierten modernen Flyer.
DIN A5 „Heft“ – Und das Profil als „Einleger“. Sollte dementsprechend ca. 1 cm umlaufend kleiner sein.
Der Flyer soll sich an dem Design der Webseite orientieren!

```html
<!DOCTYPE html>
<html lang="de">
<head>
<meta charset="utf-8">
<title>Referenzen – Flyer Veranstaltungstechnik</title>
<link href="https://fonts.googleapis.com/css2?family=Raleway:wght@800;900&family=Source+Sans+3:wght@400&display=swap" rel="stylesheet">
<style>
  :root {
    --backdrop: #868686;
    --sheet-frame: #ffffff;
    --accent-violet: #9b82c2;
    --body-text: #f2f2f2;
    --night-black: #030303;
    --haze-grey: #6e6e6e;
    --crowd-grey: #4a4a4a;
    --crowd-dark: #151515;
    --deck-light: #5c5b5c;
    --deck-grey: #3a393a;
    --deck-dark: #1b1a1b;
  }
  * { margin: 0; padding: 0; box-sizing: border-box; }
  html, body {
    width: 1200px; height: 855px; overflow: hidden;
    background: var(--backdrop);
  }
  .spread { position: relative; width: 1200px; height: 855px; }
  .sheet {
    position: absolute; top: 46px; width: 550px; height: 774px;
    background: var(--sheet-frame); padding: 7px;
  }
  .sheet--left { left: 40px; }
  .sheet--right { left: 606px; }
  .page { position: relative; width: 100%; height: 100%; overflow: hidden; }
  .page__photo { position: absolute; inset: 0; }
  .page__photo--crowd {
    background:
      radial-gradient(ellipse 22% 9% at 62% 51%, rgba(180,180,180,0.35), transparent 70%),
      radial-gradient(ellipse 14% 6% at 30% 56%, rgba(160,160,160,0.30), transparent 70%),
      radial-gradient(ellipse 60% 18% at 55% 56%, rgba(140,140,140,0.45), transparent 75%),
      radial-gradient(ellipse 35% 22% at 62% 88%, rgba(8,8,8,0.75), transparent 75%),
      radial-gradient(ellipse 30% 20% at 18% 90%, rgba(10,10,10,0.7), transparent 75%),
      radial-gradient(ellipse 25% 18% at 85% 72%, rgba(25,25,25,0.6), transparent 75%),
      radial-gradient(ellipse 30% 16% at 40% 70%, rgba(95,95,95,0.45), transparent 75%),
      linear-gradient(180deg, var(--night-black) 0%, #262626 22%, var(--crowd-grey) 40%, var(--haze-grey) 54%, #545454 62%, #333 74%, #1e1e1e 86%, var(--crowd-dark) 100%);
  }
  .page__photo--decks {
    background:
      radial-gradient(ellipse 35% 25% at 80% 30%, rgba(140,138,140,0.35), transparent 75%),
      radial-gradient(ellipse 40% 22% at 40% 42%, rgba(120,118,120,0.35), transparent 75%),
      radial-gradient(ellipse 30% 10% at 35% 8%, rgba(110,108,110,0.3), transparent 75%),
      radial-gradient(ellipse 20% 14% at 60% 62%, rgba(90,88,90,0.35), transparent 75%),
      radial-gradient(ellipse 30% 20% at 78% 80%, rgba(55,54,55,0.45), transparent 75%),
      radial-gradient(ellipse 30% 20% at 22% 85%, rgba(45,44,45,0.4), transparent 75%),
      linear-gradient(180deg, #333233 0%, var(--deck-grey) 20%, var(--deck-light) 42%, #3c3b3c 56%, #252425 66%, var(--deck-dark) 82%, #181718 100%);
  }
  .page__title {
    position: absolute; left: 37px; top: 31px;
    font: 800 32px/1 "Raleway", sans-serif;
    color: var(--accent-violet);
  }
  .ref__client {
    position: absolute;
    font: 800 15.4px/1 "Raleway", sans-serif;
    color: var(--accent-violet); white-space: nowrap;
  }
  .ref__text {
    position: absolute;
    font: 400 12.7px/15.3px "Source Sans 3", sans-serif;
    color: var(--body-text); white-space: nowrap;
  }
</style>
</head>
<body>
<main class="spread">

  <section class="sheet sheet--left">
    <div class="page">
      <div class="page__photo page__photo--crowd" role="img" aria-label="Schwarzweißfoto: jubelndes Konzertpublikum mit erhobenen Händen vor Bühnenlicht"></div>
      <h1 class="page__title">REFERENZEN</h1>

      <h2 class="ref__client" style="left:39px; top:84px;">NMK, ZTV, WSF und RBN</h2>
      <p class="ref__text" style="left:31px; top:119px;">Lorem ipsum dolor sit amet, consectetuer adipiscing elit, sed diam<br>nonummy nibh euismod tincidunt ut laoreet dolore magna aliquam</p>

      <h2 class="ref__client" style="left:35px; top:183px;">REGIERUNGSPARTEI seit 2021</h2>
      <p class="ref__text" style="left:31px; top:223px;">Lorem ipsum dolor sit amet, consectetuer adipiscing elit, sed diam<br>nonummy nibh euismod tincidunt ut laoreet dolore magna aliquam</p>

      <h2 class="ref__client" style="left:35px; top:291px;">Strandlicht International GmbH: SUNBEATS Festival 2022</h2>
      <p class="ref__text" style="left:31px; top:321px;">Lorem ipsum dolor sit amet, consectetuer adipiscing elit, sed diam<br>nonummy nibh euismod tincidunt ut laoreet dolore magna aliquam</p>
    </div>
  </section>

  <section class="sheet sheet--right">
    <div class="page">
      <div class="page__photo page__photo--decks" role="img" aria-label="Abgedunkeltes Foto: Hände eines DJs am Mischpult"></div>

      <h2 class="ref__client" style="left:42px; top:84px;">NMK, ZTV, WSF und RBN</h2>
      <p class="ref__text" style="left:42px; top:119px;">Lorem ipsum dolor sit amet, consectetuer adipiscing elit, sed diam<br>nonummy nibh euismod tincidunt ut laoreet dolore magna aliquam</p>

      <h2 class="ref__client" style="left:42px; top:183px;">REGIERUNGSPARTEI seit 2021</h2>
      <p class="ref__text" style="left:42px; top:223px;">Lorem ipsum dolor sit amet, consectetuer adipiscing elit, sed diam<br>nonummy nibh euismod tincidunt ut laoreet dolore magna aliquam</p>

      <h2 class="ref__client" style="left:42px; top:291px;">Strandlicht International GmbH: SUNBEATS Festival 2022</h2>
      <p class="ref__text" style="left:42px; top:321px;">Lorem ipsum dolor sit amet, consectetuer adipiscing elit, sed diam<br>nonummy nibh euismod tincidunt ut laoreet dolore magna aliquam</p>
    </div>
  </section>

</main>
</body>
</html>
```